TELVORA needs three flags/signs to celebrate green buildings

The template for the flag is in the attachments, and can be found on

We are looking to celebrate three of Australia's most energy efficient buildings by creating some signage for them to display. One will be an office building, one a hotel, one a shopping centre. They should include the words: "You are entering Australia's most energy efficient office/hotel/shopping centre".

So to clarify, there will need to be three different designs (office/hotel/shopping centre) but each design will need consider two sides of the flag.
Updates

Thanks to everyone who submitted a design. I have already given feedback to most. I will provide feedback to those I haven't by the end of the day. We received 30 designs all up, over half were good quality and some were very good quality. Today I'll put my favourites through to our wider team for a poll. Many thanks once again.

Target Market(s)

People entering the buildings

Industry/Entity Type

Property Management

Font styles to use
Other font styles liked:
• see logo guidelines

Requirements
Must have
• The TELVORA logo.
• The wording "You are entering Australia's most energy efficient office/hotel/shopping centre."
• It should fit into the 'flapterns' templates provided.
• The designs should refer to the TELVORA logo guidelines for style / font.
• Note: we use a seven pointed star.
Nice to have
• We have two elements that we use frequently: stars and a 'wave'. See examples of documents for ideas.
• The final design should communicate celebration with corporate elegance.

```html
<!DOCTYPE html>
<html lang="en">
<head>
<meta charset="utf-8">
<title>TELVORA – Energy Efficient Building Flags</title>
<link href="https://fonts.googleapis.com/css2?family=Arvo:wght@400;700&display=swap" rel="stylesheet">
<style>
  :root {
    --canvas: #ffffff;
    --flag-pink: #e94a8a;
    --flag-rose: #ef7fa0;
    --flag-green: #b9dc5a;
    --flag-yellow: #f6e36a;
    --flag-cream: #fdf8df;
    --pole-line: #3a2e2a;
    --pin-orange: #f07a2a;
    --pin-light: #ffffff;
    --text-brown: #4a3b1c;
    --text-dark: #1f1a12;
    --rule: #6b5a34;
    --brand-navy: #1d3550;
    --brand-teal: #2a7f8a;
  }
  * { margin: 0; padding: 0; box-sizing: border-box; }
  html, body { width: 800px; height: 1200px; overflow: hidden; background: var(--canvas); }
  .canvas { position: relative; width: 800px; height: 1200px; }

  .flag {
    position: absolute;
    top: 40px;
    width: 213px;
    height: 1120px;
    background: linear-gradient(180deg,
      var(--flag-pink) 0%,
      var(--flag-rose) 14%,
      var(--flag-green) 32%,
      var(--flag-yellow) 52%,
      var(--flag-cream) 78%,
      var(--flag-cream) 100%);
    box-shadow: 0 0 0 1px rgba(0,0,0,0.06);
    overflow: hidden;
  }
  .flag--office { left: 48px; }
  .flag--shopping { left: 294px; }
  .flag--hotel { left: 540px; }

  .flag__edge { position: absolute; top: 0; left: 0; width: 213px; height: 260px; }

  .flag__pin { position: absolute; top: 140px; left: 66px; width: 80px; height: 104px; }

  .flag__message {
    position: absolute;
    top: 370px;
    left: 14px;
    right: 14px;
    text-align: center;
    font-family: "Arvo", Georgia, serif;
    font-weight: 700;
    color: var(--text-brown);
    line-height: 1.28;
    letter-spacing: 0.5px;
  }
  .flag__rule {
    width: 90px;
    height: 3px;
    margin: 0 auto 12px;
    background: var(--rule);
    border-radius: 2px;
  }
  .flag__rule--bottom { margin: 10px auto 0; }
  .flag__small { font-size: 13px; }
  .flag__line { font-size: 21px; }
  .flag__line--wide { font-size: 19px; }
  .flag__energy { font-size: 24px; margin-top: 10px; color: var(--text-brown); }
  .flag__building {
    font-size: 31px;
    color: var(--text-dark);
    margin-top: 12px;
    line-height: 1.15;
  }
  .flag__building--long { font-size: 25px; }

  .flag__swirl {
    position: absolute;
    top: 800px;
    left: 0;
    width: 213px;
    height: 190px;
    background:
      radial-gradient(ellipse at 25% 60%, rgba(233,74,138,0.85) 0%, rgba(233,74,138,0) 38%),
      radial-gradient(ellipse at 70% 35%, rgba(246,200,60,0.85) 0%, rgba(246,200,60,0) 50%),
      radial-gradient(ellipse at 60% 80%, rgba(185,220,90,0.7) 0%, rgba(185,220,90,0) 50%);
  }

  .flag__brand {
    position: absolute;
    top: 1020px;
    left: 0;
    width: 213px;
    display: flex;
    align-items: center;
    justify-content: center;
    gap: 8px;
  }
  .flag__brand-mark { width: 16px; height: 16px; background: var(--brand-teal); }
  .flag__brand-name {
    font-family: "Arvo", Georgia, serif;
    font-weight: 700;
    font-size: 24px;
    color: var(--brand-navy);
    letter-spacing: 1px;
  }
</style>
</head>
<body>
<div class="canvas">

  <!-- Office flag -->
  <section class="flag flag--office">
    <svg class="flag__edge" viewBox="0 0 213 260"><path d="M4 258 C 20 120, 90 30, 213 8" fill="none" stroke="var(--pole-line)" stroke-width="2"/></svg>
    <svg class="flag__pin" viewBox="0 0 80 104">
      <path d="M40 102 C 30 86, 4 66, 4 40 A 36 36 0 1 1 76 40 C 76 66, 50 86, 40 102 Z" fill="var(--pin-orange)"/>
      <circle cx="40" cy="40" r="26" fill="none" stroke="var(--pin-light)" stroke-width="3"/>
      <rect x="25" y="32" width="30" height="22" rx="3" fill="var(--pin-light)"/>
      <rect x="33" y="25" width="14" height="9" rx="2" fill="none" stroke="var(--pin-light)" stroke-width="3"/>
    </svg>
    <div class="flag__message">
      <div class="flag__rule"></div>
      <div class="flag__small">YOU ARE</div>
      <div class="flag__line">ENTERING</div>
      <div class="flag__line--wide">AUSTRALIA'S</div>
      <div class="flag__line">MOST</div>
      <div class="flag__energy">ENERGY<br>EFFICIENT</div>
      <div class="flag__building">OFFICE.</div>
      <div class="flag__rule flag__rule--bottom"></div>
    </div>
    <div class="flag__swirl" role="img" aria-label="Decorative colourful swirl waves in pink, yellow and green"></div>
    <div class="flag__brand"><span class="flag__brand-mark"></span><span class="flag__brand-name">TELVORA</span></div>
  </section>

  <!-- Shopping centre flag -->
  <section class="flag flag--shopping">
    <svg class="flag__edge" viewBox="0 0 213 260"><path d="M4 258 C 20 120, 90 30, 213 8" fill="none" stroke="var(--pole-line)" stroke-width="2"/></svg>
    <svg class="flag__pin" viewBox="0 0 80 104">
      <path d="M40 102 C 30 86, 4 66, 4 40 A 36 36 0 1 1 76 40 C 76 66, 50 86, 40 102 Z" fill="var(--pin-orange)"/>
      <circle cx="40" cy="40" r="26" fill="none" stroke="var(--pin-light)" stroke-width="3"/>
      <path d="M22 28 H28 L33 48 H53 L57 33 H30" fill="none" stroke="var(--pin-light)" stroke-width="3" stroke-linejoin="round"/>
      <circle cx="35" cy="54" r="3" fill="var(--pin-light)"/>
      <circle cx="51" cy="54" r="3" fill="var(--pin-light)"/>
    </svg>
    <div class="flag__message">
      <div class="flag__rule"></div>
      <div class="flag__small">YOU ARE</div>
      <div class="flag__line">ENTERING</div>
      <div class="flag__line--wide">AUSTRALIA'S</div>
      <div class="flag__line">MOST</div>
      <div class="flag__energy">ENERGY<br>EFFICIENT</div>
      <div class="flag__building flag__building--long">SHOPING<br>CENTRE.</div>
      <div class="flag__rule flag__rule--bottom"></div>
    </div>
    <div class="flag__swirl" role="img" aria-label="Decorative colourful swirl waves in pink, yellow and green"></div>
    <div class="flag__brand"><span class="flag__brand-mark"></span><span class="flag__brand-name">TELVORA</span></div>
  </section>

  <!-- Hotel flag -->
  <section class="flag flag--hotel">
    <svg class="flag__edge" viewBox="0 0 213 260"><path d="M4 258 C 20 120, 90 30, 213 8" fill="none" stroke="var(--pole-line)" stroke-width="2"/></svg>
    <svg class="flag__pin" viewBox="0 0 80 104">
      <path d="M40 102 C 30 86, 4 66, 4 40 A 36 36 0 1 1 76 40 C 76 66, 50 86, 40 102 Z" fill="var(--pin-orange)"/>
      <circle cx="40" cy="40" r="26" fill="none" stroke="var(--pin-light)" stroke-width="3"/>
      <circle cx="40" cy="40" r="11" fill="var(--pin-light)"/>
      <path d="M22 26 V38 M20 26 V34 M24 26 V34 M22 38 V56" stroke="var(--pin-light)" stroke-width="2" stroke-linecap="round"/>
      <path d="M58 26 C 53 32, 53 40, 58 42 V56" stroke="var(--pin-light)" stroke-width="3" fill="none" stroke-linecap="round"/>
    </svg>
    <div class="flag__message">
      <div class="flag__rule"></div>
      <div class="flag__small">YOU ARE</div>
      <div class="flag__line">ENTERING</div>
      <div class="flag__line--wide">AUSTRALIA'S</div>
      <div class="flag__line">MOST</div>
      <div class="flag__energy">ENERGY<br>EFFICIENT</div>
      <div class="flag__building">HOTEL.</div>
      <div class="flag__rule flag__rule--bottom"></div>
    </div>
    <div class="flag__swirl" role="img" aria-label="Decorative colourful swirl waves in pink, yellow and green"></div>
    <div class="flag__brand"><span class="flag__brand-mark"></span><span class="flag__brand-name">TELVORA</span></div>
  </section>

</div>
</body>
</html>
```